Banner Ad for website hompage - Design Project

We need 4 banner ads for the homepage of a Rent a Car company based in dubai. We rent a wide range of cars but mainly deal in the affordable cars category. Our website colors are mainly red, white and black and I can send pictures of the website (attached) if you want something to compare possible design ideas with. The banners need to promote different messages and must be appealing to the end user. It must also use pictures of cars that exist in our fleet (Pls note: this is only if you are using cars in the banner ad)

The 4 banner ads needed are as follows:
1) should promote something along the lines of we have 20+ models available and reserve a car now (This banner should also have a reserve now button, not the actual button but it's design. The button will be made and coded by us)
2) should promote something along the lines of we offer personalised service and we look after each and every custoemr individually
3) we provide attractive rates based on daily, weekly, monthly and longer rental periods (should also incorporate a reserve now message)
4) Like us on quorvia and follow us on social media for additional offers and discounts (would like for this to have a like button design implemented in it which will be linked to quorvia.)

Also please not the picture file size is 940pixels by 400pixels

Finally: I also need the psd files for the banners.

```html
<!DOCTYPE html>
<html lang="en">
<head>
<meta charset="utf-8">
<title>Rent a Car – Homepage Banners</title>
<link rel="stylesheet" href="https://fonts.googleapis.com/css2?family=Arimo:wght@400;700&display=swap">
<style>
  :root {
    --bg-dark: #2b2b2b;
    --red: #d6301a;
    --red-deep: #b3200f;
    --red-strip: #e03a1e;
    --orange: #ff8a3d;
    --white: #ffffff;
    --ink: #222222;
    --blue: #1e5fb8;
    --photo-light: #e4e6ea;
    --photo-mid: #9aa0a8;
  }
  * { margin: 0; padding: 0; box-sizing: border-box; }
  html, body { width: 900px; height: 1200px; overflow: hidden; }
  body {
    position: relative;
    background: var(--bg-dark);
    font-family: "Arimo", Arial, sans-serif;
    color: var(--white);
  }
  .banner { position: absolute; left: 135px; width: 735px; overflow: hidden; }
  .abs { position: absolute; }
  .photo { position: absolute; z-index: 0; }

  /* Banner 1 – fleet */
  .fleet { top: 15px; height: 270px; background: var(--red); }
  .fleet .headline { left: 15px; top: 30px; font-weight: 700; line-height: 1; }
  .fleet .over { font-size: 34px; font-weight: 400; }
  .fleet .count { font-size: 68px; }
  .fleet .models { left: 15px; top: 105px; font-size: 28px; }
  .fleet .models b { font-weight: 700; }
  .reserve-btn {
    position: absolute; background: var(--red-deep);
    border: 2px solid rgba(255,255,255,.25);
    color: var(--red); font-weight: 700; letter-spacing: 6px;
    display: flex; align-items: center; justify-content: center;
    text-shadow: 0 0 1px #ff9b88;
  }
  .fleet .reserve-btn { left: 15px; top: 152px; width: 225px; height: 48px; font-size: 24px; }
  .fleet .now { left: 15px; top: 215px; font-size: 30px; }
  .fleet .now b { font-weight: 700; }
  .car-tile { border: 5px solid var(--white); background: linear-gradient(160deg, var(--photo-light), var(--photo-mid)); }

  /* Banner 2 – service */
  .service { top: 306px; height: 270px; background: var(--white); }
  .service-car {
    left: 345px; top: 100px; width: 375px; height: 155px;
    background: radial-gradient(ellipse at 55% 60%, #c9ccd1, #f4f4f5 70%);
  }
  .strip {
    position: absolute; z-index: 1; background: var(--red-strip);
    color: var(--white); font-size: 28px; font-weight: 700;
    padding: 0 12px; height: 40px; display: flex; align-items: center;
    white-space: nowrap;
  }
  .strip em { font-style: normal; color: #ffc2b0; margin-left: 8px; }
  .strip em.first { margin-left: 0; margin-right: 8px; }

  /* Banner 3 – rates */
  .rates { top: 615px; height: 255px; background: var(--red); }
  .rates .get { left: 0; width: 225px; top: 110px; text-align: center; font-size: 24px; }
  .rates .reserve-btn { left: 30px; top: 150px; width: 165px; height: 36px; font-size: 18px; letter-spacing: 4px; }
  .rates .title {
    left: 240px; top: 28px; background: var(--red-strip);
    color: var(--orange); font-weight: 700; font-size: 22px; padding: 4px 10px;
  }
  .period-list { left: 245px; top: 78px; list-style: none; font-size: 26px; }
  .period-list li { display: flex; align-items: center; height: 34px; }
  .period-list svg { margin-right: 10px; }

  /* Banner 4 – social */
  .social { top: 909px; height: 276px; background: var(--red); }
  .bubble-text {
    position: absolute; left: 300px; top: 34px; width: 400px;
    text-align: center; color: var(--ink); font-weight: 700;
    font-size: 25px; line-height: 31px; text-transform: uppercase;
  }
  .bubble-text .net { color: var(--blue); text-transform: none; }
  .bubble-text .hot { color: var(--red); }
</style>
</head>
<body>

<section class="banner fleet">
  <div class="abs headline"><span class="over">over</span> <span class="count">20+</span></div>
  <div class="abs models">vehicle <b>MODELS</b></div>
  <div class="reserve-btn">RESERVE</div>
  <div class="abs now">a car <b>NOW</b></div>
  <div class="photo car-tile" style="left:315px;top:15px;width:130px;height:90px" role="img" aria-label="Dark sedan from the fleet"></div>
  <div class="photo car-tile" style="left:455px;top:9px;width:185px;height:96px" role="img" aria-label="Silver hatchback from the fleet"></div>
  <div class="photo car-tile" style="left:321px;top:150px;width:120px;height:105px" role="img" aria-label="White sedan from the fleet"></div>
  <div class="photo car-tile" style="left:459px;top:135px;width:192px;height:120px" role="img" aria-label="Red hatchback from the fleet"></div>
</section>

<section class="banner service">
  <div class="photo service-car" role="img" aria-label="Silver hatchback, side-front view"></div>
  <div class="strip" style="left:75px;top:18px">we offer<em>PERSONALIZED</em></div>
  <div class="strip" style="left:9px;top:78px">service and we look after</div>
  <div class="strip" style="left:9px;top:138px"><em class="first">EACH</em>and<em>EVERY</em></div>
  <div class="strip" style="left:9px;top:198px">customer individually</div>
</section>

<section class="banner rates">
  <div class="photo" style="left:225px;top:0;width:510px;height:255px;background:linear-gradient(180deg,#8fa3b8 0%,#6a7480 55%,#4a4f55 100%)" role="img" aria-label="City street with traffic and tall buildings"></div>
  <div class="abs get">get your car</div>
  <div class="reserve-btn">RESERVE</div>
  <div class="abs title">ATTRACTIVE RATES BASED ON</div>
  <ul class="abs period-list">
    <li><svg width="24" height="22" viewBox="0 0 24 22"><path d="M2 12 L9 19 L22 3" fill="none" stroke="#ff5a1f" stroke-width="5"/></svg>daily</li>
    <li><svg width="24" height="22" viewBox="0 0 24 22"><path d="M2 12 L9 19 L22 3" fill="none" stroke="#ff5a1f" stroke-width="5"/></svg>weekly</li>
    <li><svg width="24" height="22" viewBox="0 0 24 22"><path d="M2 12 L9 19 L22 3" fill="none" stroke="#ff5a1f" stroke-width="5"/></svg>monthly</li>
    <li><svg width="24" height="22" viewBox="0 0 24 22"><path d="M2 12 L9 19 L22 3" fill="none" stroke="#ff5a1f" stroke-width="5"/></svg>and longer rental periods.</li>
  </ul>
</section>

<section class="banner social">
  <div class="photo" style="left:0;top:0;width:250px;height:276px;background:linear-gradient(160deg,#f2f3f5,#b9bec6)" role="img" aria-label="Dark sedan surrounded by thumbs-up like symbols"></div>
  <svg class="abs" style="left:262px;top:12px" width="460" height="252" viewBox="0 0 460 252">
    <path d="M30 6 H430 Q454 6 454 30 V196 Q454 220 430 220 H120 L60 248 L80 220 H30 Q6 220 6 196 V30 Q6 6 30 6 Z" fill="#ffffff"/>
  </svg>
  <div class="bubble-text">
    Like us on <span class="net">quorvia</span><br>
    and <span class="hot">follow us</span> on<br>
    <span class="hot">social media</span> for<br>
    additional <span class="hot">offers</span><br>
    and discounts
  </div>
</section>

</body>
</html>
```